Business Card for Restaurant Nuvelo

This project consist of creating 2 design for business card of restaurant named Nuvelo.

The attached specs below are 'ONLY SUGGESTION' if you have others ideas. You are welcome to post it.

1) Restaurant Card

Adresse:
2318 Rue des Pruniers
Montréal (Qc) H3K 2T8

Website:
www.nu-velo.ca

Phone:
438-552-0194

2) Employee Card

Name: Greta Lund
Title: Owner

Address:
2318 Rue des Pruniers
Montréal (Qc) H3K 2T8

Email:greta@nu-velo.ca
Phone Number:438-552-0194
Cellphone Number:514-730-4816

 The attached specs are 'ONLY SUGGESTION' if you have others ideas.  You are welcome to post it.

Industry/Entity Type

Restaurant

Requirements
Must have
• UV Card Spot

To print Spot UV business cards you would have to submit 2 files for each side. The first file "base" would be your regular design file as it would have been in any other case. The 2nd file "UV mask" is a black/white file. The BLACK color will indicate the areas that will be covered with the UV high gloss finish. To upload the files, please combine front design and front mask file in one P
Nice to have
• 1) The font of the logo should be ink effect
2) black background with wallpaper effect
3) The specs below are 'ONLY SUGGESTION' if you have others ideas. You are welcome to post it.

```html
<!DOCTYPE html>
<html lang="en">
<head>
<meta charset="utf-8">
<title>Nuvelo – Business Cards</title>
<link rel="stylesheet" href="https://fonts.googleapis.com/css2?family=Source+Sans+3:wght@400;600;700&family=Noto+Serif+JP:wght@700&display=swap">
<style>
  :root {
    --page: #ffffff;
    --ink: #111111;
    --card-dark: #141414;
    --card-dark-2: #2a2a2a;
    --silver: #d9d9d9;
    --tagline: #9a9a9a;
    --accent: #e0201b;
    --lantern: #0a0a0a;
    --shadow: rgba(0, 0, 0, 0.28);
  }
  * { box-sizing: border-box; margin: 0; padding: 0; }
  html, body {
    width: 1200px;
    height: 1038px;
    overflow: hidden;
    background: var(--page);
    font-family: "Source Sans 3", "Myriad Pro", Arial, sans-serif;
    color: var(--ink);
  }
  .sheet { position: relative; width: 1200px; height: 1038px; }

  .section-label {
    position: absolute;
    left: 68px;
    font-size: 17px;
    font-weight: 400;
  }
  .section-label--restaurant { top: 136px; }
  .section-label--employee { top: 537px; }

  .card {
    position: absolute;
    width: 505px;
    height: 288px;
    overflow: hidden;
    box-shadow: 4px 5px 8px var(--shadow);
  }
  .card--front { left: 70px; }
  .card--back { left: 632px; background: var(--page); }
  .row-restaurant { top: 182px; }
  .row-employee { top: 587px; }

  /* Front (dark brushed) */
  .card--front {
    background:
      repeating-linear-gradient(90deg, rgba(255,255,255,0.025) 0 1px, transparent 1px 4px),
      linear-gradient(100deg, var(--card-dark) 0%, var(--card-dark-2) 55%, var(--card-dark) 100%);
  }
  .front-lantern {
    position: absolute;
    left: 0; top: 0;
    width: 225px; height: 288px;
    background: radial-gradient(ellipse at 30% 55%, #000 0%, #050505 60%, rgba(0,0,0,0) 100%);
  }
  .brand {
    position: absolute;
    left: 216px; top: 86px;
    width: 240px;
    text-align: center;
  }
  .brand__name {
    font-size: 62px;
    font-weight: 700;
    color: var(--silver);
    line-height: 1;
    letter-spacing: 1px;
  }
  .brand__tagline {
    margin-top: 18px;
    font-size: 11px;
    font-weight: 700;
    color: var(--tagline);
    line-height: 1.3;
  }
  .brand__tagline .dot { color: var(--accent); }
  .brand__mark {
    position: absolute;
    left: 440px; top: 168px;
    width: 36px; height: 36px;
    border-radius: 50%;
    background: var(--accent);
  }

  /* Back (white) */
  .back-name {
    position: absolute;
    left: 66px; top: 48px;
    font-size: 26px;
    font-weight: 400;
    letter-spacing: 2px;
  }
  .back-title {
    position: absolute;
    left: 68px; top: 44px;
    font-size: 17px;
    line-height: 1.2;
    color: var(--accent);
  }
  .contact {
    position: absolute;
    left: 68px;
    font-size: 13px;
    line-height: 1.3;
  }
  .contact--address { top: 132px; }
  .contact--lines { top: 182px; }
  .row-employee .contact--address { top: 134px; }
  .row-employee .contact--lines { top: 182px; }

  .back-lantern {
    position: absolute;
    left: 286px; top: 0;
    width: 219px; height: 288px;
    background: var(--lantern);
    border-radius: 50% 0 0 50% / 40% 0 0 40%;
  }
  .lantern-word {
    position: absolute;
    left: 390px; top: 92px;
    width: 48px;
    font-family: "Noto Serif JP", serif;
    font-weight: 700;
    font-size: 42px;
    line-height: 1.25;
    color: var(--accent);
    text-align: center;
  }
</style>
</head>
<body>
<main class="sheet">
  <p class="section-label section-label--restaurant">1) Restaurant Card</p>

  <section class="card card--front row-restaurant">
    <div class="front-lantern" role="img" aria-label="Black paper lantern silhouette illustration"></div>
    <div class="brand">
      <p class="brand__name">Nuvelo</p>
      <p class="brand__tagline">Resto-Bar Japonais<span class="dot">•</span>Japanese Izakaya<br>Coin Gourmand</p>
    </div>
    <span class="brand__mark"></span>
  </section>

  <section class="card card--back row-restaurant">
    <p class="back-name">Nuvelo</p>
    <p class="contact contact--address">2318 Rue des Pruniers<br>Montréal (Qc) H3K 2T8</p>
    <p class="contact contact--lines">W: www.nu-velo.ca<br>T: 438-552-0194</p>
    <div class="back-lantern" role="img" aria-label="Black paper lantern illustration"></div>
    <p class="lantern-word">居<br>酒<br>屋</p>
  </section>

  <p class="section-label section-label--employee">2) Employee Card</p>

  <section class="card card--front row-employee">
    <div class="front-lantern" role="img" aria-label="Black paper lantern silhouette illustration"></div>
    <div class="brand">
      <p class="brand__name">Nuvelo</p>
      <p class="brand__tagline">Resto-Bar Japonais<span class="dot">•</span>Japanese Izakaya<br>Coin Gourmand</p>
    </div>
    <span class="brand__mark"></span>
  </section>

  <section class="card card--back row-employee">
    <p class="back-title">Owner<br>Greta Lund</p>
    <p class="contact contact--address">2318 Rue des Pruniers<br>Montréal (Qc) H3K 2T8</p>
    <p class="contact contact--lines">E: greta@nu-velo.ca<br>T: 438-552-0194<br>C: 514-730-4816</p>
    <div class="back-lantern" role="img" aria-label="Black paper lantern illustration"></div>
    <p class="lantern-word">居<br>酒<br>屋</p>
  </section>
</main>
</body>
</html>
```